Comedy Hypnotist Morlan T Show Poster

I need a poster that can send to clubs that book my show for them in turn to use to promote me/my show at their club. The poster needs to be fun and attractive, and to have a blank space at the bottom where the club(s) can add the details particular to their show. [You'll have seen these posters everywhere for bands etc.]

I'm not fussy about whether or not you use the colours from my website or any of my photos. But do capture at least the essence of the logo somewhere.

I am not like other hypnotists - I want to convey an image of amazing hilarious fun, that everyone can enjoy. [NO Watches, NO Chickens and NO Spirals]. My show is hilarious and clean.

I come across as a little geeky, and very professional. Not sleazy or creepy. But fun, professional and easy to deal with. The show is loud, buzzy and amazing. People literally laugh until they cry. I use great lighting and amazing sound to make it a real event. I aim to entertain everyone. I am never mean and don't pick on or exploit people. (Check the website for video links and more images as well as the crap posters I use now) www.morlant-shows.example.

Somehow I want people who see my poster to go - that looks like fun! Lets check it out. I would so totally go to that.

It's worth looking at the website and the youtube vid to get a feel for what I do. The pictures you'll see are colourful and active.

My logo is newish - I like it because it is simple, professional and elegant - and different from other hypnotists. In a way that is my main marketing angle - I am different from other hypnotists.

Posters should be international paper A3 size.

Target Market(s)

entertainment, comedy, hypnotist

Industry/Entity Type

Entertainment Industry

Font styles to use
Sans Serif

Requirements
Must have
• Space at the bottom (white space) for people to write the details of their event on.
• "www.morlant-shows.example" in case they want to look me up.
• "Comedy Hypnotist"
• "Morlan T"
Nice to have
• Simple and clean designs. You don't have to use the logo but if you reference it somehow that would be better so they tie together. I have included some studio photos of myself but these are not required for the poster. You can choose not to include any picture - they are there for if you want them for your design idea.
Should not have
• Spirals, Watches, Chickens

```html
<!DOCTYPE html>
<html lang="en">
<head>
<meta charset="utf-8">
<title>Morlan T – Comedy Hypnotist Poster</title>
<link rel="stylesheet" href="https://fonts.googleapis.com/css2?family=Montserrat:wght@600;700;800;900&display=swap">
<style>
  :root {
    --page: #ffffff;
    --poster-bg: #000000;
    --headline-white: #f2f2f2;
    --glow-blue: #cfe9ff;
    --glow-edge: #7fc4ff;
    --deep-blue: #0c2a66;
    --url-yellow: #e8c51c;
    --art-violet: #a025c8;
    --art-blue: #2c4cc0;
    --art-blue-dark: #10205e;
    --art-green: #3fbf2a;
    --art-red: #d0183a;
    --art-haze: #e6e0ff;
    --detail-box: #ffffff;
  }
  html, body {
    margin: 0;
    width: 1200px;
    height: 1200px;
    overflow: hidden;
    background: var(--page);
  }
  .poster {
    position: absolute;
    left: 230px;
    top: 26px;
    width: 740px;
    height: 1146px;
    background: var(--poster-bg);
    overflow: hidden;
    font-family: "Montserrat", sans-serif;
  }
  .poster__artwork {
    position: absolute;
    inset: 0;
    background:
      radial-gradient(ellipse 70px 60px at 250px 50px, var(--art-violet) 0%, transparent 100%),
      radial-gradient(ellipse 60px 90px at 420px 40px, var(--art-green) 0%, transparent 100%),
      radial-gradient(ellipse 40px 120px at 230px 160px, var(--art-violet) 0%, transparent 100%),
      radial-gradient(ellipse 90px 40px at 375px 670px, var(--art-haze) 0%, transparent 100%),
      radial-gradient(ellipse 60px 150px at 380px 780px, var(--art-violet) 0%, transparent 100%),
      radial-gradient(ellipse 80px 130px at 330px 880px, var(--art-green) 0%, transparent 100%),
      radial-gradient(ellipse 90px 110px at 210px 930px, var(--art-red) 0%, transparent 100%),
      radial-gradient(ellipse 90px 120px at 500px 920px, var(--art-red) 0%, transparent 100%),
      radial-gradient(ellipse 70px 100px at 520px 620px, var(--art-green) 0%, transparent 100%),
      radial-gradient(ellipse 210px 330px at 370px 500px, var(--art-blue) 0%, var(--art-blue-dark) 75%, transparent 100%);
    filter: blur(14px);
    opacity: 0.9;
  }
  .poster__tagline {
    position: absolute;
    top: 38px;
    left: 0;
    width: 100%;
    text-align: center;
    margin: 0;
    color: var(--headline-white);
    font-weight: 800;
    font-size: 56px;
    letter-spacing: 15px;
    text-indent: 15px;
    line-height: 1;
  }
  .poster__with {
    position: absolute;
    top: 118px;
    left: 330px;
    margin: 0;
    color: var(--headline-white);
    font-weight: 600;
    font-size: 34px;
  }
  .poster__name {
    position: absolute;
    top: 168px;
    left: 0;
    width: 100%;
    text-align: center;
    margin: 0;
    color: var(--headline-white);
    font-weight: 800;
    font-size: 124px;
    line-height: 1;
    text-shadow: 3px 4px 0 #555;
  }
  .poster__billing {
    position: absolute;
    top: 330px;
    left: 0;
    width: 100%;
    text-align: center;
    transform: rotate(-5deg);
  }
  .poster__evening {
    margin: 0 0 2px 0;
    padding-left: 10px;
    color: var(--glow-blue);
    font-weight: 800;
    font-size: 22px;
    letter-spacing: 0.5px;
    text-shadow: 0 2px 0 var(--deep-blue);
  }
  .poster__title {
    margin: 0;
    font-weight: 900;
    line-height: 0.95;
    color: var(--glow-blue);
    text-shadow:
      0 0 18px var(--glow-edge),
      4px 6px 0 var(--deep-blue),
      6px 9px 0 var(--deep-blue);
  }
  .poster__title span { display: block; }
  .poster__title-comedy { font-size: 104px; letter-spacing: -3px; }
  .poster__title-hypnotist { font-size: 106px; letter-spacing: -4px; padding-left: 10px; }
  .poster__url {
    position: absolute;
    top: 958px;
    left: 0;
    width: 100%;
    text-align: center;
    margin: 0;
    color: var(--url-yellow);
    font-weight: 800;
    font-size: 17px;
    letter-spacing: 0.5px;
  }
  .poster__details-space {
    position: absolute;
    left: 56px;
    top: 1014px;
    width: 664px;
    height: 102px;
    background: var(--detail-box);
  }
</style>
</head>
<body>
  <main class="poster">
    <div class="poster__artwork" role="img" aria-label="Glowing blue stylised performer head with eyes closed, wrapped in colourful violet, green and red smoke"></div>

    <p class="poster__tagline">EXPECT FUN</p>
    <p class="poster__with">With</p>
    <h1 class="poster__name">Morlan T</h1>

    <div class="poster__billing">
      <p class="poster__evening">AN EVENING TO REMEMBER</p>
      <h2 class="poster__title">
        <span class="poster__title-comedy">COMEDY</span>
        <span class="poster__title-hypnotist">HYPNOTIST</span>
      </h2>
    </div>

    <p class="poster__url">WWW.MORLANT-SHOWS.EXAMPLE</p>

    <div class="poster__details-space" aria-label="Space for venue event details"></div>
  </main>
</body>
</html>
```